Header/Banner Design for Website

Looking for a banner/header design for www.fixerupperdiaries.net Should be fun and whimsical, and include the name of the website, something to do with Fixer Upper Diaries or tools, and a caricature of a young, beautiful 20 something blond who the website revolves around. The website is about a young woman who bought her first house and it taking on all of the renovations and remodeling on her own for the first time.

The header/banner should include the same colors that are in the website. The width should be no more than 430 pixels, the height is flexible but the current space in the header is 85 pixels...looking for some creativity. any questions, please ask. Attached an image that she liked for the image of the woman (would like to see versions of this included)
Updates

Target Market(s)

women 20+ that are new home owners or that are tackling Fixer Upper Diaries on their own

Industry/Entity Type

Fixer Upper Diaries

Requirements
Must have
• color coordinate with the website
should feature a young, blond, female caricature
should include the name of the website

```html
<!DOCTYPE html>
<html lang="en">
<head>
<meta charset="utf-8">
<title>Fixer Upper Diaries – Header</title>
<link href="https://fonts.googleapis.com/css2?family=Open+Sans:wght@400;700&display=swap" rel="stylesheet">
<style>
  :root {
    --page-bg: #8a847d;
    --header-pink-light: #fbe3dc;
    --header-pink-deep: #f6c2b3;
    --nav-plum: #6c1244;
    --button-plum: #7d1a4f;
    --brand-berry: #8e1f58;
    --field-border: #c9c2c4;
    --field-text: #8c8c8c;
    --white: #ffffff;
    --art-burst: #fff4ef;
    --art-pink: #e0559f;
    --art-blond: #f2cf6a;
  }
  * { box-sizing: border-box; margin: 0; padding: 0; }
  html, body {
    width: 1200px;
    height: 900px;
    overflow: hidden;
  }
  body {
    background: var(--page-bg);
    font-family: "Open Sans", Arial, sans-serif;
    position: relative;
  }
  .site-header {
    position: absolute;
    left: 27px;
    top: 346px;
    width: 1154px;
    height: 196px;
    border-radius: 8px 8px 18px 18px;
    overflow: hidden;
  }
  .brand-bar {
    position: relative;
    height: 144px;
    background: linear-gradient(90deg, var(--header-pink-light) 0%, #fad7cc 55%, var(--header-pink-deep) 100%);
  }
  .mascot-art {
    position: absolute;
    left: 10px;
    top: 0;
    width: 230px;
    height: 144px;
    background:
      radial-gradient(ellipse 30% 55% at 48% 58%, var(--art-pink) 0%, rgba(224,85,159,0.6) 55%, rgba(224,85,159,0) 100%),
      radial-gradient(ellipse 18% 22% at 45% 18%, var(--art-blond) 0%, rgba(242,207,106,0) 100%),
      radial-gradient(circle at 45% 50%, var(--art-burst) 0%, #fde9e2 55%, rgba(253,233,226,0) 100%);
  }
  .brand-name {
    position: absolute;
    left: 268px;
    top: 52px;
    font-size: 33px;
    font-weight: 700;
    color: var(--brand-berry);
    letter-spacing: 0.2px;
    white-space: nowrap;
  }
  .search-form {
    position: absolute;
    left: 741px;
    top: 59px;
    display: flex;
    align-items: center;
  }
  .search-field {
    width: 234px;
    height: 38px;
    border: 1px solid var(--field-border);
    border-right: none;
    border-radius: 4px 0 0 4px;
    background: var(--white);
    padding-left: 20px;
    font-family: inherit;
    font-size: 17px;
    color: var(--field-text);
    display: flex;
    align-items: center;
  }
  .search-button {
    width: 130px;
    height: 45px;
    border-radius: 0 6px 6px 0;
    background: var(--button-plum);
    color: var(--white);
    font-size: 18px;
    display: flex;
    align-items: center;
    padding-left: 12px;
    gap: 12px;
  }
  .main-nav {
    height: 52px;
    background: var(--nav-plum);
    position: relative;
  }
  .nav-link {
    position: absolute;
    top: 50%;
    transform: translate(-50%, -50%);
    color: var(--white);
    font-weight: 700;
    font-size: 17px;
    white-space: nowrap;
  }
</style>
</head>
<body>
  <header class="site-header">
    <div class="brand-bar">
      <div class="mascot-art" role="img" aria-label="Cartoon of a young blond woman in pink overalls holding a power drill, set against a white sunburst"></div>
      <div class="brand-name">Fixer Upper Diaries</div>
      <div class="search-form">
        <div class="search-field">Search</div>
        <div class="search-button">
          <span>Search</span>
          <svg width="26" height="26" viewBox="0 0 26 26" aria-hidden="true">
            <circle cx="11" cy="8" r="5" fill="none" stroke="#ffffff" stroke-width="2"/>
            <path d="M2 23c0-5 4-8 9-8" fill="none" stroke="#ffffff" stroke-width="2" stroke-linecap="round"/>
            <path d="M19 15v9M14.5 19.5h9" stroke="#ffffff" stroke-width="2.4" stroke-linecap="round"/>
          </svg>
        </div>
      </div>
    </div>
    <nav class="main-nav">
      <span class="nav-link" style="left:97px">About Us</span>
      <span class="nav-link" style="left:288px">Products</span>
      <span class="nav-link" style="left:480px">Completed Projects</span>
      <span class="nav-link" style="left:671px">Share Your Projects</span>
      <span class="nav-link" style="left:862px">Articels</span>
      <span class="nav-link" style="left:1053px">How ti Resources</span>
    </nav>
  </header>
</body>
</html>
```